Corporate Identity for Velta - Waste management company
Letterhead, Business Card, Leaflet, Envelopes, Complimentary Card,
Simple
Marek Lisowiak
Office Management
Velta House
Tallent Wharf
Brenlow Estate
East Pelham Road
London
E14 7QN
marek@velta-waste.example
www.velta-waste.example
For our stationery we would like to include (preferably at the bottom of the page) :
Registered Office: 7th Floor Fenmore House, 42 Halden Crest Street, London, EC3R 8TD. Registered in England No: 07392846
and 6 logo certificates.
For business cards:
- please add dd and mobile number as well. We will need business cards for 3-5 different people.
No toll free number anywhere.
Delete other 2 websites and keep only one:
Footer
Please attach 7 logo certificates on letterhead and price lists.
please use just VELTA
Footer pic 1-7
Footer pic 2-7
Footer pic 3-7
Footer pic 4-7
Footer pic 5-7
Footer 6-7
Footer pic 7-7
Price List Landscape
Price List Portrait
Form 1
Form 2
Form 3
Logo certificates for letter head.

```html
<!DOCTYPE html>
<html lang="en">
<head>
<meta charset="utf-8">
<title>Velta Stationery</title>
<link href="https://fonts.googleapis.com/css2?family=Open+Sans:wght@400;600;800&display=swap" rel="stylesheet">
<style>
  :root {
    --navy: #17385a;
    --navy-deep: #0f2a45;
    --green: #7cc242;
    --green-light: #a6d86b;
    --ink: #4a4f55;
    --muted: #8a9098;
    --paper: #ffffff;
    --backdrop: #e6e7e9;
    --badge: #c9ced4;
  }
  * { box-sizing: border-box; margin: 0; padding: 0; }
  html, body { width: 1200px; height: 850px; overflow: hidden; }
  body {
    background: var(--backdrop);
    font-family: "Open Sans", Arial, sans-serif;
    color: var(--ink);
    position: relative;
  }
  .letterhead {
    position: absolute;
    top: 125px;
    width: 420px;
    height: 594px;
    background: var(--paper);
    box-shadow: 0 6px 18px rgba(0,0,0,.18);
    overflow: hidden;
  }
  .letterhead--first { left: 150px; }
  .letterhead--second { left: 615px; }
  .header-band, .footer-band { position: absolute; left: 0; width: 100%; }
  .header-band { top: 0; height: 62px; }
  .footer-band { bottom: 0; height: 40px; }
  .brand {
    position: absolute;
    display: flex;
    align-items: center;
    gap: 5px;
  }
  .letterhead .brand { top: 22px; left: 42px; }
  .brand-dot {
    width: 15px; height: 15px; border-radius: 50%;
    background: var(--green);
  }
  .brand-name {
    font-weight: 800;
    color: var(--navy);
    font-size: 19px;
    letter-spacing: .5px;
  }
  .header-contact {
    position: absolute;
    top: 22px; left: 208px;
    display: flex; gap: 22px;
    font-size: 4.6px; line-height: 1.45;
    color: var(--ink);
  }
  .letter-body {
    position: absolute;
    top: 92px; left: 42px; right: 42px;
    font-size: 6.2px; line-height: 1.5;
  }
  .recipient { margin-bottom: 9px; font-size: 7px; }
  .salutation { margin-bottom: 9px; font-size: 7px; }
  .letter-body p.copy { margin-bottom: 10px; text-align: justify; }
  .signoff { margin-top: 34px; font-size: 6.5px; }
  .signature {
    display: block; width: 48px; height: 14px; margin: 6px 0;
    background: linear-gradient(90deg, #d7dade, #eceef0);
    border-radius: 3px;
  }
  .footer-info {
    position: absolute;
    bottom: 46px; left: 42px; right: 30px;
    display: flex; justify-content: space-between; align-items: center;
  }
  .certificates { display: flex; gap: 5px; }
  .certificate {
    width: 14px; height: 14px; background: var(--badge); border-radius: 2px;
  }
  .certificate--round { border-radius: 50%; }
  .registered {
    width: 150px;
    font-size: 4.2px; line-height: 1.5; color: var(--ink);
  }
  .registered strong { color: var(--navy); font-weight: 600; }

  .business-card {
    position: absolute;
    left: 868px; top: 385px;
    width: 250px; height: 144px;
    background: var(--paper);
    box-shadow: 0 5px 14px rgba(0,0,0,.22);
    overflow: hidden;
  }
  .card-swoosh { position: absolute; left: 0; top: 0; width: 100%; height: 100%; }
  .business-card .brand { top: 62px; left: 28px; }
  .business-card .brand-name { font-size: 16px; }
  .business-card .brand-dot { width: 12px; height: 12px; }
  .card-details {
    position: absolute; top: 22px; left: 132px;
    font-size: 4.6px; line-height: 1.55;
  }
  .card-name { font-size: 6.5px; font-weight: 600; color: var(--navy); }
  .card-role { margin-bottom: 5px; color: var(--muted); }
  .card-details p + p.group { margin-top: 5px; }
</style>
</head>
<body>

<article class="letterhead letterhead--first">
  <svg class="header-band" viewBox="0 0 420 62" preserveAspectRatio="none" aria-hidden="true">
    <path d="M0 0H420V10C300 22 150 8 0 24Z" fill="var(--navy)"/>
    <path d="M0 24C150 8 300 22 420 10V13C300 26 150 13 0 28Z" fill="var(--green)"/>
  </svg>
  <div class="brand"><span class="brand-dot"></span><span class="brand-name">VELTA</span></div>
  <div class="header-contact">
    <p>Velta House, Tallent Wharf<br>Brenlow Estate, East Pelham Road<br>London E14 7QN</p>
    <p>Phone 020 7946 0321<br>marek@velta-waste.example<br>www.velta-waste.example</p>
  </div>
  <div class="letter-body">
    <p class="recipient">Someone Somebody<br>100 Arden St<br>Brisbane, Australia</p>
    <p class="salutation">Dear Someone Somebody,</p>
    <p class="copy">Lorem ipsum dolor sit amet, consectetuer adipiscing elit, sed diam nonummy nibh euismod tincidunt ut laoreet dolore magna aliquam erat volutpat. Ut wisi enim ad minim veniam, quis nostrud exerci tation ullamcorper suscipit lobortis nisl ut aliquip ex ea commodo consequat. Duis autem vel eum iriure dolor in hendrerit in vulputate velit esse molestie consequat, vel illum dolore eu feugiat nulla facilisis at vero eros et accumsan et iusto odio dignissim qui blandit praesent luptatum zzril delenit augue duis dolore te feugait nulla facilisi.</p>
    <p class="copy">Lorem ipsum dolor sit amet, consectetuer adipiscing elit, sed diam nonummy nibh euismod tincidunt ut laoreet dolore magna aliquam erat volutpat. Ut wisi enim ad minim veniam, quis nostrud exerci tation ullamcorper suscipit lobortis nisl ut aliquip ex ea commodo consequat. Duis autem vel eum iriure dolor in hendrerit in vulputate velit esse molestie consequat, vel illum dolore eu feugiat nulla facilisis at vero eros et accumsan et iusto odio dignissim qui blandit praesent luptatum zzril delenit augue duis dolore te feugait nulla facilisi.</p>
    <p class="copy">Lorem ipsum dolor sit amet, consectetuer adipiscing elit, sed diam nonummy nibh euismod tincidunt ut laoreet dolore magna aliquam erat volutpat. Ut wisi enim ad minim veniam, quis nostrud exerci tation ullamcorper suscipit lobortis nisl ut aliquip ex ea commodo consequat. Duis autem vel eum iriure dolor in hendrerit in vulputate velit esse molestie consequat, vel illum dolore eu feugiat nulla facilisis at vero eros et accumsan et iusto odio dignissim qui blandit praesent luptatum zzril delenit augue duis dolore te feugait nulla facilisi.</p>
    <div class="signoff">
      <p>Your Sincerely,<br>Tomas Reller</p>
      <span class="signature" role="img" aria-label="Handwritten signature"></span>
    </div>
  </div>
  <div class="footer-info">
    <div class="certificates">
      <span class="certificate"></span><span class="certificate certificate--round"></span><span class="certificate"></span>
      <span class="certificate certificate--round"></span><span class="certificate"></span><span class="certificate"></span>
    </div>
    <p class="registered"><strong>Registered Office:</strong> 7th Floor Fenmore House, 42 Halden Crest Street, London, EC3R 8TD.<br><strong>Registered in England No:</strong> 07392846</p>
  </div>
  <svg class="footer-band" viewBox="0 0 420 40" preserveAspectRatio="none" aria-hidden="true">
    <path d="M0 18C140 34 290 8 420 20V40H0Z" fill="var(--green)"/>
    <path d="M0 26C140 40 290 16 420 28V40H0Z" fill="var(--navy)"/>
  </svg>
</article>

<article class="letterhead letterhead--second">
  <svg class="header-band" viewBox="0 0 420 62" preserveAspectRatio="none" aria-hidden="true">
    <path d="M0 0H420V10C300 22 150 8 0 24Z" fill="var(--navy)"/>
    <path d="M0 24C150 8 300 22 420 10V13C300 26 150 13 0 28Z" fill="var(--green)"/>
  </svg>
  <div class="brand"><span class="brand-dot"></span><span class="brand-name">VELTA</span></div>
  <div class="header-contact">
    <p>Velta House, Tallent Wharf<br>Brenlow Estate, East Pelham Road<br>London E14 7QN</p>
    <p>Phone 020 7946 0321<br>marek@velta-waste.example<br>www.velta-waste.example</p>
  </div>
  <div class="letter-body">
    <p class="recipient">Someone Somebody<br>100 Arden St<br>Brisbane, Australia</p>
    <p class="salutation">Dear Someone Somebody,</p>
    <p class="copy">Lorem ipsum dolor sit amet, consectetuer adipiscing elit, sed diam nonummy nibh euismod tincidunt ut laoreet dolore magna aliquam erat volutpat. Ut wisi enim ad minim veniam, quis nostrud exerci tation ullamcorper suscipit lobortis nisl ut aliquip ex ea commodo consequat. Duis autem vel eum iriure dolor in hendrerit in vulputate velit esse molestie consequat, vel illum dolore eu feugiat nulla facilisis at vero eros et accumsan et iusto odio dignissim qui blandit praesent luptatum zzril delenit augue duis dolore te feugait nulla facilisi.</p>
    <p class="copy">Lorem ipsum dolor sit amet, consectetuer adipiscing elit, sed diam nonummy nibh euismod tincidunt ut laoreet dolore magna aliquam erat volutpat. Ut wisi enim ad minim veniam, quis nostrud exerci tation ullamcorper suscipit lobortis nisl ut aliquip ex ea commodo consequat. Duis autem vel eum iriure dolor in hendrerit in vulputate velit esse molestie consequat, vel illum dolore eu feugiat nulla facilisis at vero eros et accumsan et iusto odio dignissim qui blandit praesent luptatum zzril delenit augue duis dolore te feugait nulla facilisi.</p>
    <p class="copy">Lorem ipsum dolor sit amet, consectetuer adipiscing elit, sed diam nonummy nibh euismod tincidunt ut laoreet dolore magna aliquam erat volutpat. Ut wisi enim ad minim veniam, quis nostrud exerci tation ullamcorper suscipit lobortis nisl ut aliquip ex ea commodo consequat. Duis autem vel eum iriure dolor in hendrerit in vulputate velit esse molestie consequat, vel illum dolore eu feugiat nulla facilisis at vero eros et accumsan et iusto odio dignissim qui blandit praesent luptatum zzril delenit augue duis dolore te feugait nulla facilisi.</p>
    <div class="signoff">
      <p>Your Sincerely,<br>Tomas Reller</p>
      <span class="signature" role="img" aria-label="Handwritten signature"></span>
    </div>
  </div>
  <div class="footer-info">
    <div class="certificates">
      <span class="certificate"></span><span class="certificate certificate--round"></span><span class="certificate"></span>
      <span class="certificate certificate--round"></span><span class="certificate"></span><span class="certificate"></span>
    </div>
    <p class="registered"><strong>Registered Office:</strong> 7th Floor Fenmore House, 42 Halden Crest Street, London, EC3R 8TD.<br><strong>Registered in England No:</strong> 07392846</p>
  </div>
  <svg class="footer-band" viewBox="0 0 420 40" preserveAspectRatio="none" aria-hidden="true">
    <path d="M0 18C140 34 290 8 420 20V40H0Z" fill="var(--green)"/>
    <path d="M0 26C140 40 290 16 420 28V40H0Z" fill="var(--navy)"/>
  </svg>
</article>

<aside class="business-card">
  <svg class="card-swoosh" viewBox="0 0 250 144" preserveAspectRatio="none" aria-hidden="true">
    <path d="M0 0H250V6C160 16 70 4 0 16Z" fill="var(--navy)"/>
    <path d="M0 16C70 4 160 16 250 6V9C160 19 70 8 0 20Z" fill="var(--green)"/>
    <path d="M0 120C90 136 180 108 250 122V144H0Z" fill="var(--green)"/>
    <path d="M0 128C90 144 180 116 250 130V144H0Z" fill="var(--navy)"/>
  </svg>
  <div class="brand"><span class="brand-dot"></span><span class="brand-name">VELTA</span></div>
  <div class="card-details">
    <p class="card-name">Marek Lisowiak</p>
    <p class="card-role">Office Management</p>
    <p>Velta House, Tallent Wharf<br>Brenlow Estate, East Pelham Road<br>London E14 7QN</p>
    <p class="group">DD 020 7946 0322<br>Mobile 07700 900481<br>marek@velta-waste.example<br>www.velta-waste.example</p>
  </div>
</aside>

</body>
</html>
```